New business card for my lawn and landscape business

Dorrin Yard and Building is a full-service lawn care, landscaping, and light construction company serving Paragould and the Northeast Arkansas region. The business is owned and operated by Marcus Toller, with a reputation for hands-on, detail-oriented service, dependable crews, and quality results for both residential and commercial clients. A well regarded business with great reviews.
Owner Marcus Toller
Dorrinyardandbuilding.example

Target Market(s)

Commercial, Middle, and upper class in north east Arkansas

Industry/Entity Type

Lawn maintenance and landscape

Contact Information for Business Card

Dorrin Yard And Building Professional lawn care, landscaping, and property improvement in Northeast Arkansas. • lawn maintenance •lawn treatments and weed control • exterior projects • Custom landscape design & installation • Sod, trees, rock & drainage solutions • Residential & commercial services Reliable. Detailed. Done right.

Requirements
Must have
• Business name, service area, list of some of our services, clean design that represents
Nice to have
• Unique. Different design element than just grass because its already in n the logo. Picture of a warm season (south) lawn or landscape. Pictures of the type of work we do

```html
<!DOCTYPE html>
<html lang="en">
<head>
<meta charset="utf-8">
<title>Dorrin Yard and Building – Business Card</title>
<link href="https://fonts.googleapis.com/css2?family=Montserrat:wght@400;500;700&display=swap" rel="stylesheet">
<style>
  :root {
    --stage: #b3b3b3;
    --card-light: #f2f0f4;
    --card-dark: #242424;
    --green: #6aab3f;
    --green-deep: #3f8a34;
    --green-mid: #5aa245;
    --band-gray: #5a5a5e;
    --text-gray: #444446;
    --text-light: #e6e6e6;
    --white: #ffffff;
  }
  * { box-sizing: border-box; margin: 0; padding: 0; }
  html, body {
    width: 1200px; height: 554px; overflow: hidden;
    background: var(--stage);
    font-family: "Montserrat", sans-serif;
  }
  .card {
    position: absolute;
    width: 524px; height: 299px;
    border-radius: 18px;
    overflow: hidden;
  }
  .card-front { left: 68px; top: 128px; background: var(--card-light); }
  .card-back { left: 607px; top: 127px; background: var(--card-dark); }

  .front-art { position: absolute; inset: 0; }

  .owner-name {
    position: absolute; left: 27px; top: 44px;
    font-size: 25px; font-weight: 700; letter-spacing: 0.5px;
    color: var(--green);
  }
  .owner-title {
    position: absolute; left: 27px; top: 74px;
    font-size: 15px; font-weight: 500;
    color: var(--text-gray);
  }

  .brand {
    position: absolute;
    display: flex; align-items: center; gap: 10px;
  }
  .brand-dot { flex: none; border-radius: 50%; background: var(--green); }
  .brand-name {
    font-weight: 700; color: var(--green);
    line-height: 1.1; text-transform: uppercase;
  }
  .card-front .brand { left: 318px; top: 44px; width: 190px; }
  .card-front .brand-dot { width: 22px; height: 22px; }
  .card-front .brand-name { font-size: 19px; }

  .card-back .brand { left: 150px; top: 70px; width: 240px; }
  .card-back .brand-dot { width: 28px; height: 28px; }
  .card-back .brand-name { font-size: 24px; }

  .contact-list {
    position: absolute; left: 28px; top: 193px;
    list-style: none;
  }
  .contact-list li {
    display: flex; align-items: center; gap: 9px;
    height: 24px;
    font-size: 14.5px; color: var(--white);
  }
  .contact-list svg { width: 12px; height: 12px; flex: none; fill: var(--white); }

  .services {
    position: absolute; left: 26px; top: 216px; width: 474px;
    font-size: 10.4px; line-height: 16.8px;
    color: var(--text-light);
    text-align: justify; text-align-last: center;
  }
  .services .lead { color: var(--green); }
  .services .dot { color: var(--green); }
</style>
</head>
<body>

<section class="card card-front">
  <svg class="front-art" viewBox="0 0 524 299" width="524" height="299">
    <defs>
      <linearGradient id="lawnTone" x1="0" y1="0" x2="0" y2="1">
        <stop offset="0" stop-color="#4e9c3c"/>
        <stop offset="0.5" stop-color="#3f8f33"/>
        <stop offset="1" stop-color="#2f7a2a"/>
      </linearGradient>
    </defs>
    <path class="band-gray" fill="#5a5a5e"
      d="M0 150 C90 128 190 130 300 160 C400 188 480 160 524 127 L524 172 C460 188 400 184 300 168 C190 150 90 150 0 172 Z"/>
    <g role="img" aria-label="Close-up photo of green lawn grass">
      <path fill="url(#lawnTone)"
        d="M0 176 C90 160 190 160 300 176 C400 190 470 184 524 170 L524 299 L0 299 Z"/>
    </g>
  </svg>

  <h1 class="owner-name">MARCUS TOLLER</h1>
  <p class="owner-title">OWNER</p>

  <div class="brand">
    <span class="brand-dot"></span>
    <span class="brand-name">Dorrin Yard and Building</span>
  </div>

  <ul class="contact-list">
    <li>
      <svg viewBox="0 0 24 24" aria-hidden="true"><path d="M6.6 10.8a15 15 0 0 0 6.6 6.6l2.2-2.2c.3-.3.7-.4 1-.2 1.1.4 2.3.6 3.6.6.6 0 1 .4 1 1V20c0 .6-.4 1-1 1A17 17 0 0 1 3 4c0-.6.4-1 1-1h3.5c.6 0 1 .4 1 1 0 1.3.2 2.5.6 3.6.1.3 0 .7-.2 1z"/></svg>
      (870) 555-0148
    </li>
    <li>
      <svg viewBox="0 0 24 24" aria-hidden="true"><path d="M2 5h20v14H2z M2 5l10 8 10-8" fill="#ffffff"/><path d="M3 6l9 7 9-7" fill="none" stroke="#3f8f33" stroke-width="1.6"/></svg>
      info@Dorrinyardandbuilding.example
    </li>
    <li>
      <svg viewBox="0 0 24 24" aria-hidden="true"><circle cx="12" cy="12" r="10"/><path d="M2 12h20M12 2c3 3 3 17 0 20M12 2c-3 3-3 17 0 20" fill="none" stroke="#3f8f33" stroke-width="1.4"/></svg>
      Dorrinyardandbuilding.example
    </li>
  </ul>
</section>

<section class="card card-back">
  <div class="brand">
    <span class="brand-dot"></span>
    <span class="brand-name">Dorrin Yard and Building</span>
  </div>

  <p class="services">
    <span class="lead">Dorrin Yard &amp; Building Professional lawn care, landscaping, and property improvement in Northeast Arkansas</span>
    <span class="dot">•</span> lawn maintenance
    <span class="dot">•</span> lawn treatments &amp; weed control
    <span class="dot">•</span> exterior projects
    <span class="dot">•</span> Custom landscape design &amp; installation
    <span class="dot">•</span> Sod, trees, rock &amp; drainage solutions
    <span class="dot">•</span> Residential &amp; commercial services Reliable. Detailed. Done right.
  </p>
</section>

</body>
</html>
```